Rovilent.com Trucking Company Website

Need a website designed (no content) for a trucking company, specializing in trucking of ocean containers (intermodal Trucking). Heavy emphasis on technology, using latest technology, providing unabated visibility and realtime information.
clean minimalist industrial website
example:
https://www.belquarn.com/

Target Market(s)

Professional Business Consumer corporate and small business

Industry/Entity Type

Trucking Company

Number of Pages Required

5+ page

Requirements
Must have
• Industrial Design, simple informative, for a busy professional to view and get the necessary information with out the distractions.
• Blog Page
• Client Log-In on the front page
• Technology page - showing our intensive investments in technology
Nice to have
• If ANY images included, MUST be USA related. Example if include an image of a truck, ensure its a USA model. Do the research.
• included our business card for sample of Logo
• Doesnt not have to be the same color schemes.
Should not have
• moving images

```html
<!DOCTYPE html>
<html lang="en">
<head>
<meta charset="utf-8">
<title>Rovilent – Intermodal Trucking</title>
<link href="https://fonts.googleapis.com/css2?family=Roboto:wght@300;400;500;700&display=swap" rel="stylesheet">
<style>
:root{
  --blue:#0f57a6;
  --blue-dark:#0a3f80;
  --blue-bright:#1f8fd8;
  --ink:#1e1e1e;
  --text:#555;
  --muted:#888;
  --line:#dcdfe4;
  --soft:#f2f4f7;
  --white:#fff;
}
*{box-sizing:border-box;margin:0;padding:0}
html,body{width:1200px;height:2329px;overflow:hidden}
body{font-family:'Roboto',Arial,sans-serif;color:var(--ink);background:var(--white);position:relative}
.abs{position:absolute}

/* header */
.site-header{position:absolute;top:0;left:0;width:1200px;height:73px;background:var(--white);border-top:4px solid var(--blue-dark)}
.brand{position:absolute;left:50px;top:20px;font-weight:700;font-size:24px;color:var(--blue);letter-spacing:1px}
.main-nav{position:absolute;top:28px;left:0;font-size:14px;color:var(--ink)}
.main-nav span{position:absolute;white-space:nowrap}
.chat-link{position:absolute;left:925px;top:28px;font-size:14px}
.call-btn{position:absolute;left:1006px;top:22px;width:143px;height:31px;background:var(--blue);color:#fff;border-radius:3px;font-size:13px;font-weight:700;text-align:center;line-height:31px}

/* hero */
.hero{position:absolute;top:73px;left:0;width:1200px;height:486px;background:linear-gradient(110deg,#c9c1b2 0%,#8f99a6 35%,#4f5a66 60%,#3b4450 80%,#6c737a 100%)}

/* welcome */
.welcome{position:absolute;top:559px;left:0;width:1200px;height:244px;background:var(--white)}
.welcome h1{position:absolute;left:50px;width:726px;top:12px;text-align:center;font-size:21px;font-weight:500}
.welcome h1 b{color:var(--blue);font-weight:500}
.dashed{position:absolute;border-top:1px dashed #7a8aa3}
.welcome p{position:absolute;left:62px;width:702px;top:64px;font-size:12.4px;line-height:19px;color:var(--text);text-align:center;font-weight:300}
.like-strip{position:absolute;height:34px;border:1px solid var(--line);border-radius:17px;background:#fff}
.like-thumb{position:absolute;width:18px;height:16px;border:1.5px solid #bbb;border-radius:3px}
.like-btn{position:absolute;height:14px;width:36px;background:#4267b2;color:#fff;font-size:9px;font-weight:700;line-height:14px;text-align:center;border-radius:2px}
.like-txt{position:absolute;font-size:9px;color:#333;white-space:nowrap}
.card-photo{position:absolute;left:803px;top:8px;width:393px;height:225px;background:linear-gradient(180deg,#e6e8eb,#c7ccd3)}
.card-name{position:absolute;left:0;width:393px;top:70px;text-align:center;color:var(--blue);font-size:44px;font-weight:700;letter-spacing:2px}
.card-sub{position:absolute;left:0;width:393px;top:126px;text-align:center;color:#555;font-size:16px;letter-spacing:8px}
.card-url{position:absolute;left:0;width:393px;top:196px;text-align:center;color:var(--blue-dark);font-size:10px;font-weight:500}

/* technology */
.tech{position:absolute;top:803px;left:0;width:1200px;height:326px;background:var(--soft)}
.tab{position:absolute;top:20px;height:43px;font-size:18px;font-weight:500;line-height:41px;text-align:center}
.tab.active{left:438px;width:168px;border:1px solid var(--blue);color:var(--blue);background:#fff;border-radius:2px}
.tab.plain{left:620px;width:146px}
.feature{position:absolute;top:115px;width:180px;text-align:center}
.feature .pic{width:140px;height:140px;margin:0 auto;border-radius:50%;display:flex;align-items:center;justify-content:center}
.feature h3{margin-top:12px;font-size:18px;font-weight:500;line-height:23px}

/* contact */
.contact{position:absolute;top:1129px;left:0;width:600px;height:345px;background:linear-gradient(120deg,#0e4c95,#1a7bc8 70%,#2b97dd)}
.contact h2{position:absolute;left:0;width:600px;top:16px;text-align:center;color:#fff;font-size:25px;font-weight:500}
.field{position:absolute;height:33px;background:#fff;border-radius:2px;font-size:12px;color:#999;padding:9px 12px}
.send-btn{position:absolute;left:233px;top:289px;width:135px;height:33px;background:#fff;border-radius:3px;font-size:13px;font-weight:500;text-align:center;line-height:33px}
.promo{position:absolute;top:1129px;left:600px;width:600px;height:345px;background:linear-gradient(180deg,#8d939a 0%,#5c636b 45%,#2e3338 100%)}
.promo-text{position:absolute;left:200px;top:78px;width:250px;text-align:center;color:#fff;font-weight:500;text-shadow:0 1px 3px rgba(0,0,0,.4)}

/* stats */
.stats{position:absolute;top:1474px;left:0;width:1200px;height:154px;background:#fff}
.stat{position:absolute;top:12px;width:300px;text-align:center}
.stat .lead{font-size:18px;font-weight:300}
.stat .num{font-size:44px;font-weight:700;color:var(--blue);margin-top:10px}
.stat .cap{font-size:13px;color:#444;margin-top:18px}

/* blog */
.blog{position:absolute;top:1628px;left:0;width:1200px;height:497px;background:var(--soft)}
.blog h2{position:absolute;left:0;width:1200px;top:12px;text-align:center;font-size:22px;font-weight:500}
.blog h2 b{color:var(--blue);font-weight:500}
.post{position:absolute;top:108px;width:253px;height:353px;background:#fff}
.post .pic{height:187px}
.post h3{margin:20px 19px 0;font-size:17.5px;font-weight:500}
.post p{margin:10px 19px 0;font-size:12.5px;line-height:19px;color:var(--text);font-weight:300}
.post .meta{position:absolute;left:19px;right:19px;top:313px;border-top:3px solid #eee;padding-top:12px;font-size:11.5px;color:#444;display:flex;justify-content:space-between}

/* like bar */
.like-bar{position:absolute;top:2125px;left:0;width:1200px;height:74px;background:#fff}

/* footer */
.site-footer{position:absolute;top:2199px;left:0;width:1200px;height:130px;background:#fff;border-top:3px solid var(--blue-dark)}
.foot-nav{position:absolute;top:53px;font-size:13px;font-weight:500}
.foot-nav span{position:absolute;white-space:nowrap}
.foot-rule{position:absolute;left:60px;top:80px;width:1080px;border-top:1px solid var(--line)}
.foot-links{position:absolute;top:93px;font-size:11.5px;color:#333}
.foot-links span{position:absolute;white-space:nowrap}
.foot-brand{position:absolute;left:997px;top:33px;font-weight:700;font-size:26px;color:var(--blue);letter-spacing:1px}
.social{position:absolute;top:92px;width:16px;height:16px;background:var(--blue);border-radius:2px}
</style>
</head>
<body>

<header class="site-header">
  <div class="brand">Rovilent</div>
  <nav class="main-nav">
    <span style="left:357px">Our Company</span>
    <span style="left:475px">Technology</span>
    <span style="left:581px">Blog</span>
    <span style="left:646px">Log In</span>
  </nav>
  <div class="chat-link">Chat
    <svg width="14" height="12" viewBox="0 0 14 12" style="vertical-align:-1px"><path d="M1 2h9v6H4l-3 3z" fill="none" stroke="#222" stroke-width="1.4"/><path d="M11 4h2v6l-2-2H6" fill="none" stroke="#222" stroke-width="1.2"/></svg>
  </div>
  <div class="call-btn">Call: +1 555 010 4477</div>
</header>

<section class="hero" role="img" aria-label="American semi truck hauling heavy equipment on a highway under a cloudy sky"></section>

<section class="welcome">
  <h1>Welcome to <b>Rovilent</b></h1>
  <div class="dashed" style="left:50px;top:50px;width:726px"></div>
  <p>Sed ut perspiciatis unde omnis iste natus error sit voluptatem accusantium doloremque laudantium, totam rem aperiam, eaque ipsa quae ab illo chomu inventore veritatis et quasi architecto beatae vitae dicta sunt explicabo. Nemo enim ipsam voluptatem quia voluptas sit aspernatur aut odit aut fugit, sed quia consequun. Lorem ipsum dolor sit amet, consectetur einem adipiscing elit, sed do eiusmod tempor incididunt ut labore et dolore magna aliqua. Ut enim ad minim veniam, quis nostrud exercitation ullamco laboris nisi ut aliquip ex ea commodo consequat. Duis aute irure dolor in reprehend.</p>
  <div class="abs" style="left:50px;top:204px;width:212px;border-top:1px solid var(--line)"></div>
  <div class="abs" style="left:566px;top:204px;width:210px;border-top:1px solid var(--line)"></div>
  <div class="like-strip" style="left:263px;top:187px;width:303px">
    <div class="like-thumb" style="left:14px;top:8px"></div>
    <div class="abs" style="left:38px;top:6px;height:20px;border-left:1px solid var(--line)"></div>
    <div class="like-btn" style="left:82px;top:9px">Like</div>
    <div class="like-txt" style="left:122px;top:10px">You and 4k others like this.</div>
  </div>
  <div class="card-photo" role="img" aria-label="Business card with a white truck photo in the background">
    <div class="card-name">Rovilent</div>
    <div class="card-sub">CONSULTING</div>
    <div class="abs" style="left:0;top:210px;width:393px;border-top:1px solid #888"></div>
    <div class="card-url">www.rovilent.com</div>
  </div>
</section>

<section class="tech">
  <div class="tab active">Our Technology</div>
  <div class="tab plain">Our Services</div>
  <div class="dashed" style="left:66px;top:74px;width:1068px"></div>

  <div class="feature" style="left:42px">
    <div class="pic" role="img" aria-label="Road photo with steering wheel icon" style="background:radial-gradient(circle,#8a8d90,#45484b)">
      <svg width="52" height="52" viewBox="0 0 52 52"><circle cx="26" cy="26" r="22" fill="none" stroke="#fff" stroke-width="5"/><circle cx="26" cy="26" r="5" fill="#fff"/><path d="M6 24h14M32 24h14M26 31v16" stroke="#fff" stroke-width="5"/></svg>
    </div>
    <h3>It Starts With<br>Safety</h3>
  </div>
  <div class="feature" style="left:225px">
    <div class="pic" role="img" aria-label="Truck on a highway with signal icon" style="background:radial-gradient(circle,#c7c9cf,#7d8089)">
      <svg width="52" height="44" viewBox="0 0 52 44"><circle cx="26" cy="22" r="5" fill="#fff"/><path d="M17 12a13 13 0 0 0 0 20M35 12a13 13 0 0 1 0 20M10 5a22 22 0 0 0 0 34M42 5a22 22 0 0 1 0 34" fill="none" stroke="#fff" stroke-width="3"/></svg>
    </div>
    <h3>Safer<br>Together</h3>
  </div>
  <div class="feature" style="left:409px">
    <div class="pic" role="img" aria-label="Fuel savings graphic over a road photo" style="background:radial-gradient(circle,#9a9b9c,#4d4f52)">
      <span style="color:#fff;font-size:28px;font-weight:300">7%</span>
      <svg width="26" height="30" viewBox="0 0 26 30" style="margin:0 6px"><rect x="3" y="4" width="14" height="22" fill="#fff"/><path d="M17 10l5 3v10" stroke="#fff" stroke-width="2" fill="none"/></svg>
      <span style="color:#fff;font-size:18px;font-weight:300">4.5%</span>
    </div>
    <h3>Fuel<br>Savings</h3>
  </div>
  <div class="feature" style="left:593px">
    <div class="pic" role="img" aria-label="Network map over a landscape photo" style="background:radial-gradient(circle,#9a8c58,#2f3d55)">
      <svg width="40" height="48" viewBox="0 0 40 48"><rect x="10" y="4" width="20" height="26" rx="3" fill="#fff"/><rect x="13" y="8" width="14" height="8" fill="#2f3d55"/><path d="M4 46l8-14M36 46l-8-14" stroke="#fff" stroke-width="3"/></svg>
    </div>
    <h3>Network<br>Operations</h3>
  </div>
  <div class="feature" style="left:777px">
    <div class="pic" role="img" aria-label="Dispatcher with headset and link icon" style="background:radial-gradient(circle,#8b6a55,#3b2f2a)">
      <svg width="44" height="44" viewBox="0 0 44 44"><rect x="4" y="16" width="22" height="12" rx="6" transform="rotate(-45 15 22)" fill="none" stroke="#fff" stroke-width="4"/><rect x="18" y="16" width="22" height="12" rx="6" transform="rotate(-45 29 22)" fill="none" stroke="#fff" stroke-width="4"/></svg>
    </div>
    <h3>Team<br>Work</h3>
  </div>
  <div class="feature" style="left:960px">
    <div class="pic" role="img" aria-label="Trucks on a desert highway with pairing icon" style="background:radial-gradient(circle,#a9a39a,#5b5a58)">
      <svg width="40" height="38" viewBox="0 0 40 38"><rect x="4" y="6" width="14" height="20" rx="2" fill="#fff"/><rect x="22" y="6" width="14" height="20" rx="2" fill="#fff"/><rect x="0" y="28" width="40" height="4" fill="#fff"/></svg>
    </div>
    <h3>Intelligent<br>Pairing</h3>
  </div>
</section>

<section class="contact">
  <h2>Feel Free to Mail</h2>
  <div class="field" style="left:50px;top:72px;width:240px">Name *</div>
  <div class="field" style="left:311px;top:72px;width:240px">Email *</div>
  <div class="field" style="left:50px;top:124px;width:240px">Subject</div>
  <div class="field" style="left:311px;top:124px;width:240px">Phone Number</div>
  <div class="field" style="left:50px;top:176px;width:501px;height:93px">Write Your Message Here...</div>
  <div class="send-btn">SEND MESSAGE</div>
</section>
<section class="promo" role="img" aria-label="Blue truck driving along a coastal road">
  <div class="promo-text">
    <div style="font-size:31px;line-height:34px">THE REAL</div>
    <div style="font-size:46px;line-height:44px">KING</div>
    <div style="font-size:27px;line-height:32px">OF</div>
    <div style="font-size:28px;line-height:34px">INVESTMENTS</div>
    <div style="font-size:27px;line-height:34px">IN TECHNOLOGY</div>
  </div>
</section>

<section class="stats">
  <div class="stat" style="left:75px"><div class="lead">Free Running</div><div class="num">60,000 +</div><div class="cap">Container Access</div></div>
  <div class="stat" style="left:450px"><div class="lead">OVER</div><div class="num">30</div><div class="cap">Years of Experience In Transportation</div></div>
  <div class="stat" style="left:825px"><div class="lead">Authorized</div><div class="num">13,000 +</div><div class="cap">Carriers In Third-Party Network</div></div>
</section>

<section class="blog">
  <h2>Latest <b>Blog &amp; Views</b></h2>
  <div class="dashed" style="left:51px;top:51px;width:1098px"></div>

  <article class="post" style="left:51px">
    <div class="pic" role="img" aria-label="Cargo ship docked at a port at dusk" style="background:linear-gradient(180deg,#3b3f86,#2a2440 70%,#4a3b3a)"></div>
    <h3>Ullamcorper Parturien</h3>
    <p>Morbi leo risus, porta ac consectur at eros. Maecenas sed diam eget risus varius blandit sit amet non.</p>
    <div class="meta"><span>&#128197; 28 October, 2020</span><span>&#128172;15</span></div>
  </article>
  <article class="post" style="left:334px">
    <div class="pic" role="img" aria-label="Container port cranes lit at night" style="background:linear-gradient(180deg,#2f4f86,#1e2e4c 65%,#6a4a2a)"></div>
    <h3>Excepteur Sint Occaecat</h3>
    <p>Lorem ipsum dolor sit amet, consectetur adipiscing elit, sed do eiusmod tempor incididunt ut lab.</p>
    <div class="meta"><span>&#128197; 27 October, 2020</span><span>&#128172;11</span></div>
  </article>
  <article class="post" style="left:615px">
    <div class="pic" role="img" aria-label="Aerial view of a container ship loaded with colourful containers" style="background:linear-gradient(180deg,#3e6f83,#9a6b4a 55%,#2c6f8c)"></div>
    <h3>Neque Porro Quisquam</h3>
    <p>Sed ut perspiciatis unde omnis iste natus error sit voluptatem accusantium doloremque laudanti.</p>
    <div class="meta"><span>&#128197; 26 October, 2020</span><span>&#128172;10</span></div>
  </article>
  <article class="post" style="left:896px">
    <div class="pic" role="img" aria-label="Trucks at a dark loading dock" style="background:linear-gradient(180deg,#2d3e55,#1a2230);position:relative">
      <div style="position:absolute;left:113px;top:80px;width:28px;height:28px;background:#2a9fd6;border-radius:3px"></div>
    </div>
    <h3>Quis Autem Vel Eum</h3>
    <p>Nemo enim ipsam voluptatem quia voluptas sit aspernatur aut odit aut fugit, sed quia consetur.</p>
    <div class="meta"><span>&#128197; 25 October, 2020</span><span>&#128172;15</span></div>
  </article>
</section>

<section class="like-bar">
  <div class="abs" style="left:66px;top:37px;width:310px;border-top:1px solid var(--line)"></div>
  <div class="abs" style="left:826px;top:37px;width:308px;border-top:1px solid var(--line)"></div>
  <div class="like-strip" style="left:376px;top:14px;width:450px;height:46px;border-radius:23px">
    <div class="like-thumb" style="left:22px;top:13px"></div>
    <div class="abs" style="left:56px;top:8px;height:28px;border-left:1px solid var(--line)"></div>
    <div class="like-btn" style="left:120px;top:15px;width:46px">Like</div>
    <div class="like-txt" style="left:172px;top:16px;font-size:11px">You and 4k others like this.</div>
  </div>
</section>

<footer class="site-footer">
  <svg class="abs" style="left:60px;top:51px" width="13" height="13" viewBox="0 0 13 13"><circle cx="5" cy="5" r="4" fill="none" stroke="#333" stroke-width="1.6"/><path d="M8 8l4 4" stroke="#333" stroke-width="1.8"/></svg>
  <nav class="foot-nav">
    <span style="left:94px">Help &amp; Contact</span>
    <span style="left:212px">Services</span>
    <span style="left:289px">Our Technology</span>
    <span style="left:408px">Log In</span>
  </nav>
  <div class="foot-brand">Rovilent</div>
  <div class="foot-rule"></div>
  <div class="foot-links">
    <span style="left:60px">About</span>
    <span style="left:112px">Blog</span>
    <span style="left:155px">Jobs</span>
    <span style="left:200px">Public Policy</span>
    <span style="left:285px">Sitemap</span>
    <span style="left:348px">Partners</span>
    <span style="left:932px">© 2016–2017</span>
    <span style="left:1023px">Privacy</span>
  </div>
  <div class="social" style="left:1075px"></div>
  <div class="social" style="left:1098px"></div>
  <div class="social" style="left:1121px"></div>
</footer>

</body>
</html>
```